Pathways to Brightmoor Land Ventures

size of the ad - 8”x 10.75" plus 0.25" bleed
I would like an ad for a magazine that will stand out and make people want to read the ad.
The ad should not be crowded and people reading the ad will be able to read the text.
I would like it to be a creative and modern-day design.
the list of topics should not be the focus of the ad.
the text is attached.
If you decide to use people in the ad then please no ladies.
please note that leave over 1 inch for the bottom of the footer

```html
<!DOCTYPE html>
<html lang="en">
<head>
<meta charset="utf-8">
<title>Real Estate Course – Pathways to Brightmoor Land Ventures</title>
<link rel="stylesheet" href="https://fonts.googleapis.com/css2?family=Poppins:wght@400;500;600;700;800&display=swap">
<style>
  :root {
    --navy: #0a2590;
    --sky: #0f98d8;
    --ink: #1c1b20;
    --paper: #ffffff;
    --stage: #262d36;
    --rule: #b9bcc4;
  }
  * { margin: 0; padding: 0; box-sizing: border-box; }
  html, body {
    width: 1200px; height: 2736px; overflow: hidden;
    background: var(--stage);
    font-family: "Poppins", sans-serif;
  }
  .ad {
    position: absolute; left: 54px; top: 664px;
    width: 910px; height: 1173px;
    transform: scale(1.2); transform-origin: top left;
    background: var(--paper); overflow: hidden;
  }
  .ad__art { position: absolute; inset: 0; }
  .masthead { position: absolute; left: 97px; top: 84px; color: var(--paper); }
  .masthead__title {
    font-weight: 800; font-size: 63px; line-height: 56px; letter-spacing: -0.5px;
  }
  .masthead__subtitle {
    margin-top: 20px; font-weight: 400; font-size: 37px; line-height: 44px;
  }
  .headline {
    position: absolute; left: 100px; top: 484px;
    font-weight: 800; font-size: 46px; line-height: 43px; color: var(--ink);
    letter-spacing: -0.3px;
  }
  .topics-title {
    position: absolute; left: 100px; top: 685px;
    color: var(--sky); font-weight: 500; font-size: 40px; line-height: 42px;
  }
  .topics { position: absolute; top: 783px; list-style: none; }
  .topics--left { left: 100px; width: 186px; }
  .topics--right { left: 316px; width: 189px; }
  .topics li {
    position: relative; padding-left: 11px;
    font-weight: 600; font-size: 14.8px; line-height: 16px; color: var(--ink);
    border-bottom: 1.5px dashed var(--rule);
    padding-bottom: 7px; margin-bottom: 9.5px;
  }
  .topics li::before {
    content: ""; position: absolute; left: 0; top: 6px;
    width: 5px; height: 5px; border-radius: 50%; background: var(--navy);
  }
  .topics--right li { margin-bottom: 12.5px; }
  .session-badge {
    position: absolute; left: 464px; top: 419px; width: 354px; height: 354px;
    border-radius: 50%; background: var(--sky); color: var(--paper);
    text-align: center;
  }
  .session-badge::after {
    content: ""; position: absolute; inset: 19px;
    border: 1.5px solid var(--paper); border-radius: 50%;
  }
  .session-badge__place { margin-top: 72px; font-weight: 800; font-size: 50px; line-height: 50px; }
  .session-badge__detail { font-size: 23px; line-height: 24px; }
  .session-badge__start { margin-top: 20px; font-size: 23px; line-height: 26px; }
  .session-badge__offer { margin-top: 15px; font-weight: 800; font-size: 24px; line-height: 22px; }
  .early-bird {
    position: absolute; left: 544px; top: 796px;
    font-size: 27px; line-height: 28px; color: var(--ink);
  }
  .early-bird__title { margin-bottom: 15px; }
</style>
</head>
<body>
  <main class="ad">
    <svg class="ad__art" width="910" height="1173" viewBox="0 0 910 1173">
      <defs>
        <linearGradient id="photoTone" x1="0" y1="0" x2="1" y2="1">
          <stop offset="0" stop-color="#f3f1ea"/>
          <stop offset="0.45" stop-color="#e6dccb"/>
          <stop offset="0.8" stop-color="#c9a878"/>
          <stop offset="1" stop-color="#b88a4e"/>
        </linearGradient>
      </defs>
      <rect class="hero-photo" x="420" y="0" width="490" height="420" fill="url(#photoTone)"
            role="img" aria-label="Photo of a hand placing a small wooden model house on a table, with a jar of coins in soft light"/>
      <path class="wave-accent" fill="var(--sky)"
            d="M0,478 C120,470 210,380 300,338 C380,300 470,330 535,372 C600,405 660,350 735,285 C790,238 860,240 910,300 V1173 H0 Z"/>
      <path class="wave-paper" fill="var(--paper)"
            d="M0,478 C120,476 220,400 305,360 C385,322 470,350 535,390 C600,428 665,372 740,308 C795,262 860,266 910,330 V1173 H0 Z"/>
      <path class="masthead-shape" fill="var(--navy)"
            d="M0,0 H540 C500,50 470,90 477,130 C485,190 560,250 576,300 C590,345 570,385 530,390 C470,395 420,345 340,350 C250,356 200,440 120,462 C80,472 40,465 0,458 Z"/>
      <path class="footer-wave" fill="var(--navy)"
            d="M0,1048 C60,1010 110,990 160,992 C260,996 330,1095 420,1095 C540,1095 660,968 760,968 C820,968 870,1000 910,1027 V1173 H0 Z"/>
      <path class="footer-accent" fill="var(--sky)"
            d="M456,1173 C560,1110 720,1070 910,1053 V1173 Z"/>
    </svg>

    <header class="masthead">
      <h1 class="masthead__title">Real Estate<br>Course</h1>
      <p class="masthead__subtitle">Pathways to<br>Brightmoor Land<br>Ventures</p>
    </header>

    <h2 class="headline">Investing In<br>Knowledge Is<br>Investing In<br>Opportunities</h2>

    <h3 class="topics-title">Topics:<br>partial listing</h3>
    <ul class="topics topics--left">
      <li>Real estate investment strategies</li>
      <li>Due diligence</li>
      <li>Financing</li>
      <li>Underwriting</li>
      <li>Property management</li>
    </ul>
    <ul class="topics topics--right">
      <li>Real estate Legal basics</li>
      <li>Sourcing deals</li>
      <li>Syndication</li>
      <li>Dealing with brokers</li>
      <li>Tax fundamentals</li>
    </ul>

    <section class="session-badge">
      <p class="session-badge__place">Larkfield</p>
      <p class="session-badge__detail">10 –Tuesday evenings<br>sessions</p>
      <p class="session-badge__start">Starting Feb.28</p>
      <p class="session-badge__offer">Limited Partial S<br>cholarships</p>
    </section>

    <section class="early-bird">
      <p class="early-bird__title">Early Bird Special</p>
      <p>For those that<br>started or would<br>like to go into<br>real estate</p>
    </section>
  </main>
</body>
</html>
```